SHOP PAGE PRODUCT GRAPHICS 900x600 FOR E COMMERCE SITE. 5 TOTAL

NEED 5 GRAPHICS 900x600 MADE FOR MY SHOP PAGE HERE:

feel free to omit any redundant content http://plinkoridge.com/qx/darel/shop.jpg Custom Image For Products On Shop Page:AL A CARTE:Buy Video Ads On an As Needed Basis$37 PER VIDEO!INCLUDES:1 Video Ad ($149 VALUE) 1 Video Ad Converted To Square Ratio ($39 VALUE)1 Video Ad Converted To Vertical Ratio ($39 VALUE)1 Video Ad Converted To Pinwheeler Cover Video ($129 VALUE)VALUE $3564 Videos NOW ONLY $14960% OFF$37 PER VIDEO!INSTRUCTIONS FOR IMAGE:SHOW PHOTOS OF ALL PHOTOS SIZES USING SAME VIDEO. LET ME KNOW IF YOU NEED ONE I HAVE MP4 FILES FOR ALL SIZES SHOW PHOTOS OF ALL PHOTOS SIZES USING SAME VIDEO. LET ME KNOW IF YOU NEED ONE I HAVE MP4 FILES FOR ALL SIZES OR YOU CAN USE IMAGES FROM MY WEBSITE WWW.QUILLNESTFILMWORKS.COM PLEASE SCROLL DOWN ON HOMEPAGE AND SEE “VIDEO SIZES” SECTION AND USE THESE IMAGES IF YOU HAVE TO….I WANT THE IMAGE TO SHOW ALL THE DIFFERENT VIDEO SIZES THEY GET SO IT LOOKS LIKE A LOT OF VALUE…._______________________________________________________________________________________SUBSCRIPTION:Big Discounts Per Video When You Sign Up For A Monthly Subscription$25 PER VIDEO!INCLUDES:1 Video Ad ($149 VALUE)1 Video Ad Converted To Square Ratio ($39 VALUE)1 Video Ad Converted To Vertical Ratio ($39 VALUE)1 Video Ad Converted To Pinwheeler Cover Video ($129 VALUE)VALUE $3564 Videos NOW ONLY $9975% OFF$25 PER VIDEO!INSTRUCTIONS FOR IMAGE:SHOW PHOTOS OF ALL PHOTOS SIZES USING SAME VIDEO. LET ME KNOW IF YOU NEED ONE I HAVE MP4 FILES FOR ALL SIZES SHOW PHOTOS OF ALL PHOTOS SIZES USING SAME VIDEO. LET ME KNOW IF YOU NEED ONE I HAVE MP4 FILES FOR ALL SIZES OR YOU CAN USE IMAGES FROM MY WEBSITE WWW.QUILLNESTFILMWORKS.COM PLEASE SCROLL DOWN ON HOMEPAGE AND SEE “VIDEO SIEZES” SECTION AND USE THESE IMAGES IF YOU HAVE TO….I WANT THE IMAGE TO SHOW ALL THE DIFFERENT VIDEO SIZES THEY GET SO IT LOOKS LIKE A LOT OF VALUE….___________________________________________________________________________QUILLNEST MONTHLY CONTENT CALENDAR SUBSCRIPTION:Daily Content and Custom Branded Videos For Every Day.LESS THAN $10 PER VIDEO!INCLUDES:30 Videos ($1470 VALUE)VALUE $1470/mth30 Videos & Daily Content Only $299/mth90% OFF$10 PER VIDEO!INSTRUCTIONS FOR IMAGE:SHOW A PIC OF A CALENDAR WITH CONTENT/TEXT AND VIDEO FOR EACH DAY. SEE MY WEBSITE AT https://quillnestfilmworks.com/calendar/june and use something from here for this image. I WANT IT TO BE CLEAR THAT THEY WILL RECEIVE A VIDEO FOR EVERY DAY AND CONTENT TO POST TO THEIR SOCIAL MEDIA PAGES ______________________________________________________________________________HOLIDAY THEMED PACKAGECelebrate the Holidays with videos$58 PER VIDEO!INCLUDES:17 HOLIDAY THEMED VIDEOS ($1683 VALUE)VALUE $168317 Videos Only $99935% OFF$58 PER VIDEO!INSTRUCTIONS FOR IMAGE:SHOW A COLLAGE OF HOLIDAY THEMED VIDEOS. YOU CAN FIND SOME HOLIDAY THEMED VIDEOS ON MY WEBSITE HERE: https://quillnestfilmworks.com/categories FROM DROP DOWN MENU CHOOSE LABOR DAY, MEMORIAL DAY, HALLOWEEN, CHRISTMAS, NEW YEARS, NEW YEARS, VALENTINES TO SEE EXAMPLES OF HOLIDAY THEMED VIDEOS FOR THIS IMAGE. __________________________________________________________________SEASONAL THEMED PACKAGEWelcome every season with a new video$74 PER VIDEO!4 Seasonal Themed Videos ($396 VALUE)VALUE $3964 Videos Only $29925% OFF$74 PER VIDEO!INSTRUCTIONS FOR IMAGE:SHOW A COLLAGE OF SEASONAL THEMED VIDEOS. YOU CAN FIND THE SEASONAL THEMED VIDEOS ON MY WEBSITE FRAMLY PAGE HERE: https://framly.com/user51268403 SUMMER, SPRING, FALL, WINTER

Target Market(s)

B2B

Industry/Entity Type

Video Production

Colors

Designer to choose colors to be used in the design.

Requirements
Must have
• NEED 5 GRAPHICS MADE FOR MY SHOP PAGE HERE: 900x600 ://plinkoridge.com/qx/darel/shop.jpg
• Custom Image For Products On Shop Page:
• AL A CARTE:
• Buy Video Ads On an As Needed Basis
• $37 PER VIDEO!
• INCLUDES:
• 1 Video Ad ($149 VALUE)
• 1 Video Ad Converted To Square Ratio ($39 VALUE)
• 1 Video Ad Converted To Vertical Ratio ($39 VALUE)
• 1 Video Ad Converted To Pinwheeler Cover Video ($129 VALUE)
• VALUE $356
• 4 Videos NOW ONLY $149
• 60% OFF
• $37 PER VIDEO!
• INSTRUCTIONS FOR IMAGE:
• SHOW PHOTOS OF ALL PHOTOS SIZES USING SAME VIDEO. LET ME KNOW IF YOU NEED ONE I HAVE MP4 FILES FOR ALL SIZES SHOW PHOTOS OF ALL PHOTOS SIZES USING SAME VIDEO. LET ME KNOW IF YOU NEED ONE I HAVE MP4 FILES FOR ALL SIZES OR YOU CAN USE IMAGES FROM MY WEBSITE WWW.QUILLNESTFILMWORKS.COM PLEASE SCROLL DOWN ON HOMEPAGE AND SEE “VIDEO SIZES” SECTION AND USE THESE IMAGES IF YOU HAVE TO….I WANT THE IMAGE TO SHOW ALL THE DIFFERENT VIDEO SIZES THEY GET SO IT LOOKS LIKE A LOT OF VALUE….
• _______________________________________________________________________________________
• SUBSCRIPTION:
• Big Discounts Per Video When You Sign Up For A Monthly Subscription
• $25 PER VIDEO!
• INCLUDES:
• 1 Video Ad ($149 VALUE)
• VALUE $356
• 4 Videos NOW ONLY $99
• 75% OFF
• $25 PER VIDEO!
• INSTRUCTIONS FOR IMAGE:
• SHOW PHOTOS OF ALL PHOTOS SIZES USING SAME VIDEO. LET ME KNOW IF YOU NEED ONE I HAVE MP4 FILES FOR ALL SIZES SHOW PHOTOS OF ALL PHOTOS SIZES USING SAME VIDEO. LET ME KNOW IF YOU NEED ONE I HAVE MP4 FILES FOR ALL SIZES OR YOU CAN USE IMAGES FROM MY WEBSITE WWW.QUILLNESTFILMWORKS.COM PLEASE SCROLL DOWN ON HOMEPAGE AND SEE “VIDEO SIEZES” SECTION AND USE THESE IMAGES IF YOU HAVE TO….I WANT THE IMAGE TO SHOW ALL THE DIFFERENT VIDEO SIZES THEY GET SO IT LOOKS LIKE A LOT OF VALUE….
• ___________________________________________________________________________
• QUILLNEST MONTHLY CONTENT CALENDAR SUBSCRIPTION:
• Daily Content and Custom Branded Videos For Every Day.
• LESS THAN $10 PER VIDEO!
• INCLUDES:
• 30 Videos ($1470 VALUE)
• VALUE $1470/mth
• 30 Videos & Daily Content Only $299/mth
• 90% OFF
• $10 PER VIDEO!
• INSTRUCTIONS FOR IMAGE:
• SHOW A PIC OF A CALENDAR WITH CONTENT/TEXT AND VIDEO FOR EACH DAY. SEE MY WEBSITE AT https://quillnestfilmworks.com/calendar/june and use something from here for this image. I WANT IT TO BE CLEAR THAT THEY WILL RECEIVE A VIDEO FOR EVERY DAY AND CONTENT TO POST TO THEIR SOCIAL MEDIA PAGES
• ______________________________________________________________________________
• HOLIDAY THEMED PACKAGE
• Celebrate the Holidays with videos
• $58 PER VIDEO!
• INCLUDES:
• 17 HOLIDAY THEMED VIDEOS ($1683 VALUE)
• VALUE $1683
• 17 Videos Only $999
• 35% OFF
• $58 PER VIDEO!
• INSTRUCTIONS FOR IMAGE:
• SHOW A COLLAGE OF HOLIDAY THEMED VIDEOS. YOU CAN FIND SOME HOLIDAY THEMED VIDEOS ON MY WEBSITE HERE: https://quillnestfilmworks.com/categories FROM DROP DOWN MENU CHOOSE LABOR DAY, MEMORIAL DAY, HALLOWEEN, CHRISTMAS, NEW YEARS, NEW YEARS, VALENTINES TO SEE EXAMPLES OF HOLIDAY THEMED VIDEOS FOR THIS IMAGE.
• __________________________________________________________________
• SEASONAL THEMED PACKAGE
• Welcome every season with a new video
• $74 PER VIDEO!
• 4 Seasonal Themed Videos ($396 VALUE)
• VALUE $396
• 4 Videos Only $299
• 25% OFF
• $74 PER VIDEO!
• INSTRUCTIONS FOR IMAGE:
• SHOW A COLLAGE OF SEASONAL THEMED VIDEOS. YOU CAN FIND THE SEASONAL THEMED VIDEOS ON MY WEBSITE FRAMLY PAGE HERE: https://framly.com/user51268403 SUMMER, SPRING, FALL, WINTER
Nice to have
• NEED 5 GRAPHICS MADE FOR MY SHOP PAGE HERE: http://plinkoridge.com/qx/darel/shop.jpg 900x600
• AL A CARTE:
• $37 PER VIDEO!
• INCLUDES:
• 1 Video Ad ($149 VALUE)
• VALUE $356
• 4 Videos NOW ONLY $149
• 60% OFF
• $37 PER VIDEO!
• INSTRUCTIONS FOR IMAGE:
• SUBSCRIPTION:
• $25 PER VIDEO!
• INCLUDES:
• 1 Video Ad ($149 VALUE)
• VALUE $356
• 4 Videos NOW ONLY $99
• 75% OFF
• $25 PER VIDEO!
• INSTRUCTIONS FOR IMAGE:
• INCLUDES:
• 30 Videos ($1470 VALUE)
• VALUE $1470/mth
• 90% OFF
• $10 PER VIDEO!
• INSTRUCTIONS FOR IMAGE:
• HOLIDAY THEMED PACKAGE
• $58 PER VIDEO!
• INCLUDES:
• VALUE $1683
• 17 Videos Only $999
• 35% OFF
• $58 PER VIDEO!
• INSTRUCTIONS FOR IMAGE:
• SEASONAL THEMED PACKAGE
• $74 PER VIDEO!
• VALUE $396
• 4 Videos Only $299
• 25% OFF
• $74 PER VIDEO!
• INSTRUCTIONS FOR IMAGE:
Should not have
• AL A CARTE:
• $37 PER VIDEO!
• INCLUDES:
• 1 Video Ad ($149 VALUE)
• VALUE $356
• 4 Videos NOW ONLY $149
• 60% OFF
• $37 PER VIDEO!
• INSTRUCTIONS FOR IMAGE:
• SUBSCRIPTION:
• $25 PER VIDEO!
• INCLUDES:
• 1 Video Ad ($149 VALUE)
• VALUE $356
• 4 Videos NOW ONLY $99
• 75% OFF
• $25 PER VIDEO!
• INSTRUCTIONS FOR IMAGE:
• INCLUDES:
• 30 Videos ($1470 VALUE)
• VALUE $1470/mth
• 90% OFF
• $10 PER VIDEO!
• INSTRUCTIONS FOR IMAGE:
• HOLIDAY THEMED PACKAGE
• $58 PER VIDEO!
• INCLUDES:
• VALUE $1683
• 17 Videos Only $999
• 35% OFF
• $58 PER VIDEO!
• INSTRUCTIONS FOR IMAGE:
• SEASONAL THEMED PACKAGE
• $74 PER VIDEO!
• VALUE $396
• 4 Videos Only $299
• 25% OFF
• $74 PER VIDEO!
• INSTRUCTIONS FOR IMAGE:

```html
<!DOCTYPE html>
<html lang="en">
<head>
<meta charset="utf-8">
<title>Al a Carte – Video Ads Offer</title>
<link rel="stylesheet" href="https://fonts.googleapis.com/css2?family=Montserrat:wght@500;600;700;800&display=swap">
<style>
  :root {
    --yellow-top: #fffb00;
    --yellow-deep: #ffc800;
    --magenta: #e21ce6;
    --violet: #7a0fc4;
    --navy: #1c0a9c;
    --heading-purple: #9a12c9;
    --badge-ink: #3b1670;
    --badge-ring: #a310d6;
    --price-red: #ee0a0a;
    --ink: #111111;
    --struck-ink: #34448e;
  }
  * { margin: 0; padding: 0; box-sizing: border-box; }
  html, body { width: 1200px; height: 800px; overflow: hidden; background: #ffffff; }
  .offer-card {
    position: relative;
    width: 1200px;
    height: 800px;
    overflow: hidden;
    font-family: "Montserrat", Arial, sans-serif;
    color: var(--ink);
  }
  .backdrop { position: absolute; inset: 0; width: 1200px; height: 800px; }
  .format-label { font-family: "Montserrat", Arial, sans-serif; font-weight: 600; fill: var(--ink); }

  .offer-copy {
    position: absolute;
    left: 82px;
    top: 70px;
    font-size: 25px;
    font-weight: 500;
    line-height: 34.3px;
  }
  .offer-title {
    font-size: 37px;
    font-weight: 800;
    color: var(--heading-purple);
    line-height: 44px;
    margin-bottom: 1px;
    letter-spacing: 0.5px;
  }
  .offer-copy p { white-space: nowrap; }
  .accent { color: var(--price-red); font-weight: 700; }
  .struck {
    color: var(--struck-ink);
    text-decoration: line-through;
    text-decoration-color: var(--price-red);
    text-decoration-thickness: 2px;
  }

  .discount-badge {
    position: absolute;
    left: 815px;
    top: 414px;
    width: 386px;
    height: 386px;
    border-radius: 50%;
    border: 11px solid var(--badge-ring);
    background: radial-gradient(circle at 40% 35%, var(--yellow-top), var(--yellow-deep));
    color: var(--badge-ink);
    display: flex;
    flex-direction: column;
    align-items: center;
    justify-content: center;
    text-align: center;
  }
  .badge-percent { font-size: 94px; font-weight: 600; line-height: 88px; }
  .badge-label { font-size: 36px; font-weight: 500; line-height: 40px; }
  .badge-off { font-size: 108px; font-weight: 700; line-height: 98px; }
</style>
</head>
<body>
<main class="offer-card">
  <svg class="backdrop" viewBox="0 0 900 600" aria-hidden="true">
    <defs>
      <linearGradient id="sun-fill" x1="0" y1="0" x2="1" y2="1">
        <stop offset="0" stop-color="#fffb00"/>
        <stop offset="1" stop-color="#ffc400"/>
      </linearGradient>
      <linearGradient id="night-fill" x1="0" y1="0" x2="1" y2="0">
        <stop offset="0" stop-color="#7a0fc4"/>
        <stop offset="0.45" stop-color="#3a0c9e"/>
        <stop offset="1" stop-color="#1c0a9c"/>
      </linearGradient>
    </defs>
    <rect class="sky" width="900" height="600" fill="url(#sun-fill)"/>
    <path class="accent-band" d="M0,290 C50,400 150,505 310,478 L900,162 L900,600 L0,600 Z" fill="#e21ce6"/>
    <path class="night-field" d="M0,318 C55,425 160,530 320,500 L900,182 L900,600 L0,600 Z" fill="url(#night-fill)"/>

    <g class="format-icons" fill="none" stroke="#111" stroke-width="3">
      <!-- wide format -->
      <g class="film-frame">
        <rect x="481" y="79" width="94" height="47"/>
        <line x1="493" y1="79" x2="493" y2="126"/>
        <line x1="563" y1="79" x2="563" y2="126"/>
        <g fill="#111" stroke="none">
          <rect x="484" y="84" width="6" height="5"/><rect x="484" y="94" width="6" height="5"/><rect x="484" y="104" width="6" height="5"/><rect x="484" y="114" width="6" height="5"/>
          <rect x="566" y="84" width="6" height="5"/><rect x="566" y="94" width="6" height="5"/><rect x="566" y="104" width="6" height="5"/><rect x="566" y="114" width="6" height="5"/>
        </g>
        <text class="format-label" x="528" y="109" font-size="17" text-anchor="middle" stroke="none">MP4</text>
      </g>
      <!-- square format -->
      <g class="film-frame">
        <rect x="598" y="79" width="62" height="47"/>
        <line x1="608" y1="79" x2="608" y2="126"/>
        <line x1="650" y1="79" x2="650" y2="126"/>
        <g fill="#111" stroke="none">
          <rect x="600" y="84" width="5" height="5"/><rect x="600" y="94" width="5" height="5"/><rect x="600" y="104" width="5" height="5"/><rect x="600" y="114" width="5" height="5"/>
          <rect x="653" y="84" width="5" height="5"/><rect x="653" y="94" width="5" height="5"/><rect x="653" y="104" width="5" height="5"/><rect x="653" y="114" width="5" height="5"/>
        </g>
        <text class="format-label" x="629" y="109" font-size="17" text-anchor="middle" stroke="none">MP4</text>
      </g>
      <!-- cover format -->
      <g class="film-frame">
        <rect x="679" y="79" width="101" height="47"/>
        <line x1="689" y1="79" x2="689" y2="126"/>
        <line x1="770" y1="79" x2="770" y2="126"/>
        <g fill="#111" stroke="none">
          <rect x="681" y="84" width="5" height="5"/><rect x="681" y="94" width="5" height="5"/><rect x="681" y="104" width="5" height="5"/><rect x="681" y="114" width="5" height="5"/>
          <rect x="773" y="84" width="5" height="5"/><rect x="773" y="94" width="5" height="5"/><rect x="773" y="104" width="5" height="5"/><rect x="773" y="114" width="5" height="5"/>
        </g>
        <text class="format-label" x="729.5" y="107" font-size="10" text-anchor="middle" stroke="none">PINWHEELER</text>
      </g>
      <!-- vertical format -->
      <g class="film-frame">
        <rect x="796" y="60" width="65" height="85"/>
        <line x1="806" y1="60" x2="806" y2="145"/>
        <line x1="851" y1="60" x2="851" y2="145"/>
        <g fill="#111" stroke="none">
          <rect x="798" y="65" width="5" height="5"/><rect x="798" y="76" width="5" height="5"/><rect x="798" y="87" width="5" height="5"/><rect x="798" y="98" width="5" height="5"/><rect x="798" y="109" width="5" height="5"/><rect x="798" y="120" width="5" height="5"/><rect x="798" y="131" width="5" height="5"/>
          <rect x="854" y="65" width="5" height="5"/><rect x="854" y="76" width="5" height="5"/><rect x="854" y="87" width="5" height="5"/><rect x="854" y="98" width="5" height="5"/><rect x="854" y="109" width="5" height="5"/><rect x="854" y="120" width="5" height="5"/><rect x="854" y="131" width="5" height="5"/>
        </g>
        <text class="format-label" x="828.5" y="88" font-size="17" text-anchor="middle" stroke="none">M</text>
        <text class="format-label" x="828.5" y="106" font-size="17" text-anchor="middle" stroke="none">P</text>
        <text class="format-label" x="828.5" y="124" font-size="17" text-anchor="middle" stroke="none">4</text>
      </g>
    </g>
  </svg>

  <section class="offer-copy">
    <h1 class="offer-title">AL A CARTE :</h1>
    <p>Buy Video Ads On an As Needed Basis</p>
    <p><span class="accent">$37</span> PER VIDEO!</p>
    <p>INCLUDES:</p>
    <p><span class="accent">1</span> Video Ad (<span class="accent">$149</span> VALUE)</p>
    <p><span class="accent">1</span> Video Ad Converted To Square Ratio (<span class="accent">$39</span> VALUE)</p>
    <p><span class="accent">1</span> Video Ad Converted To Vertical Ratio (<span class="accent">$39</span> VALUE)</p>
    <p><span class="accent">1</span> Video Ad Converted To Pinwheeler Cover Video (<span class="accent">$129</span> VALUE)</p>
    <p class="struck">VALUE $356</p>
    <p><span class="accent">4</span> Videos NOW ONLY <span class="accent">$149</span></p>
    <p><span class="accent">60%</span> OFF</p>
    <p><span class="accent">$37</span> PER VIDEO!</p>
  </section>

  <div class="discount-badge">
    <span class="badge-percent">60%</span>
    <span class="badge-label">AL A CARTE</span>
    <span class="badge-off">OFF</span>
  </div>
</main>
</body>
</html>
```